Home web page re-vamp

I would like a stylish new home page design for a clients website.
I have included a sitemap to give some guidance.
The site needs to show off the design capabilitiesof the client

```html
<!DOCTYPE html>
<html lang="en">
<head>
<meta charset="utf-8">
<title>Northvale Architects – Home</title>
<link rel="stylesheet" href="https://fonts.googleapis.com/css2?family=Open+Sans:wght@400;600&display=swap">
<style>
  :root {
    --page-bg: #262b35;
    --sidebar-bg: #2f3541;
    --sidebar-rule: #3a414e;
    --logo-rule: #272c36;
    --nav-text: #d7dbe1;
    --icon-muted: #c4c9d1;
    --brand: #6fb8cc;
    --content-bg: #ffffff;
    --card-top: #e6e6e6;
    --card-bottom: #ffffff;
    --card-border: #d3d3d3;
    --ink: #262b35;
    --ink-soft: #555555;
    --caption-bg: rgba(10, 10, 12, 0.82);
    --footer-text: #d7dbe1;
  }
  * { box-sizing: border-box; margin: 0; padding: 0; }
  html, body { width: 1200px; height: 692px; overflow: hidden; }
  body {
    background: var(--page-bg);
    font-family: "Open Sans", Arial, sans-serif;
    position: relative;
  }
  .sidebar {
    position: absolute; left: 99px; top: 0; width: 248px; height: 692px;
    background: var(--sidebar-bg);
  }
  .brand {
    height: 138px; border-bottom: 2px solid var(--logo-rule);
    display: flex; align-items: center; justify-content: center; gap: 8px;
  }
  .brand-mark { width: 12px; height: 12px; border-radius: 50%; background: var(--brand); }
  .brand-name { color: var(--brand); font-weight: 600; font-size: 22px; letter-spacing: 0.2px; }
  .main-nav { list-style: none; margin: 3px 0 0 31px; width: 185px; }
  .main-nav li {
    height: 41px; display: flex; align-items: center; gap: 10px;
    border-bottom: 1px solid var(--sidebar-rule);
    color: var(--nav-text); font-size: 11.5px; padding-left: 8px;
  }
  .main-nav li:last-child { border-bottom: none; }
  .main-nav svg { width: 12px; height: 12px; fill: var(--icon-muted); flex: none; }
  .social { margin: 30px 0 0 40px; color: var(--nav-text); font-size: 11px; }
  .social-row { display: flex; gap: 22px; margin-top: 20px; padding-left: 3px; }
  .social-dot { width: 11px; height: 11px; border-radius: 50%; background: var(--icon-muted); }

  .content {
    position: absolute; left: 347px; top: 0; width: 755px; height: 595px;
    background: var(--content-bg);
  }
  .slider {
    position: absolute; left: 25px; top: 23px; width: 707px; height: 335px;
    background: linear-gradient(180deg, #c9d4dd 0%, #8fa2ad 30%, #6d7f6a 48%, #d9dbd8 62%, #3b3b3d 80%, #cfcfcc 100%);
  }
  .slider-caption {
    position: absolute; left: 0; bottom: 0; width: 100%; height: 51px;
    background: var(--caption-bg); display: flex; align-items: center;
    padding: 0 18px 0 25px; justify-content: space-between;
  }
  .slider-caption p { color: #fff; font-size: 17px; }
  .slider-arrows { display: flex; gap: 1px; }
  .slider-arrows span {
    width: 25px; height: 24px; background: #3a3a3c; display: flex;
    align-items: center; justify-content: center;
  }
  .slider-arrows svg { width: 8px; height: 12px; stroke: #aaa; fill: none; stroke-width: 1.2; }

  .features {
    position: absolute; left: 25px; top: 380px; width: 710px;
    display: grid; grid-template-columns: repeat(4, 168px); gap: 12px;
  }
  .feature {
    height: 187px; border: 1px solid var(--card-border);
    background: linear-gradient(180deg, var(--card-top), var(--card-bottom));
    text-align: center; padding-top: 27px;
  }
  .feature svg { width: 34px; height: 34px; fill: var(--ink); }
  .feature h2 {
    font-weight: 400; font-size: 16px; line-height: 21px; color: var(--ink);
    margin-top: 10px;
  }
  .feature p {
    font-family: Arial, Helvetica, sans-serif; font-size: 11px; line-height: 19px;
    color: var(--ink-soft); margin: 8px 12px 0;
  }

  .footer {
    position: absolute; left: 347px; top: 595px; width: 755px; height: 97px;
    background: var(--sidebar-bg); text-align: center; color: var(--footer-text);
  }
  .footer-nav { list-style: none; display: flex; justify-content: center; margin-top: 28px; font-size: 11.5px; }
  .footer-nav li + li::before { content: "/"; margin: 0 18px; }
  .copyright { font-size: 11.5px; margin-top: 12px; }
</style>
</head>
<body>
  <aside class="sidebar">
    <div class="brand"><span class="brand-mark"></span><span class="brand-name">Northvale</span></div>
    <ul class="main-nav">
      <li><svg viewBox="0 0 12 12"><circle cx="6" cy="3.5" r="2.8"/><path d="M1 12c0-4 2-5.5 5-5.5s5 1.5 5 5.5z"/></svg>About Us</li>
      <li><svg viewBox="0 0 12 12"><circle cx="4.5" cy="7" r="3.5"/><circle cx="9.5" cy="3" r="2.3"/></svg>Services</li>
      <li><svg viewBox="0 0 12 12"><circle cx="6" cy="4" r="2"/><circle cx="2" cy="5" r="1.5"/><circle cx="10" cy="5" r="1.5"/><path d="M2.5 11c0-3 1.5-4 3.5-4s3.5 1 3.5 4z"/></svg>Our Clients</li>
      <li><svg viewBox="0 0 12 12"><path d="M0 1h12v10H0zM1.5 9.5h9L7.5 5 5 8 3.5 6.5z" fill-rule="evenodd"/></svg>Gallery</li>
      <li><svg viewBox="0 0 12 12"><path d="M6 0a6 6 0 1 0 0 12A6 6 0 0 0 6 0zm0 1.5a4.5 4.5 0 1 1 0 9 4.5 4.5 0 0 1 0-9zM3 4h6v1.2H3zm0 3h6v1.2H3z" fill-rule="evenodd"/></svg>Health &amp; Safety</li>
      <li><svg viewBox="0 0 12 12"><path d="M0 1.5h12v9H0zM1.3 2.8v6.4h9.4V2.8zM2.3 4h3v2.5h-3zm4 0h3.4v1H6.3zm0 2h3.4v1H6.3zM2.3 7.5h7.4v.9H2.3z" fill-rule="evenodd"/></svg>Specification Sheets</li>
      <li><svg viewBox="0 0 12 12"><path d="M2.5 0.5l2 2.5-1.3 1.5c.8 1.7 2.2 3.1 3.9 3.9L8.6 7l2.9 2-1 2.5C5 11.5.5 7 .5 1.5z"/></svg>Contact Us</li>
    </ul>
    <div class="social">
      <p>Connect with our social network :</p>
      <div class="social-row"><span class="social-dot"></span><span class="social-dot"></span><span class="social-dot"></span><span class="social-dot"></span><span class="social-dot"></span></div>
    </div>
  </aside>

  <main class="content">
    <section class="slider" role="img" aria-label="Photo of a rooftop terrace with wicker lounge sofas overlooking a lake and mountains">
      <div class="slider-caption">
        <p>We are a interior design company</p>
        <div class="slider-arrows">
          <span><svg viewBox="0 0 8 12"><path d="M6 1L1.5 6 6 11"/></svg></span>
          <span><svg viewBox="0 0 8 12"><path d="M2 1l4.5 5L2 11"/></svg></span>
        </div>
      </div>
    </section>

    <section class="features">
      <article class="feature">
        <svg viewBox="0 0 34 34"><circle cx="17" cy="10" r="5.5"/><circle cx="7.5" cy="12" r="4"/><circle cx="26.5" cy="12" r="4"/><path d="M8 31c0-9 4-12 9-12s9 3 9 12z"/><path d="M0 28c0-7 3-10 7.5-10 2 0 3 .5 4 1.3C8.5 21.5 7 25 7 28z"/><path d="M34 28c0-7-3-10-7.5-10-2 0-3 .5-4 1.3 3 2.2 4.5 5.7 4.5 8.7z"/></svg>
        <h2>Why Us</h2>
        <p>7 Days from quotation to delivery using the latest technology</p>
      </article>
      <article class="feature">
        <svg viewBox="0 0 34 34"><path d="M31 2c1 1-8 13-12 16l-3-3C19 11 30 1 31 2z"/><path d="M14 17l3 3c0 5-4 9-14 9 3-2 2-5 4-8 2-3 5-4 7-4z"/></svg>
        <h2>Architects &amp; Designers</h2>
        <p>Advice on colours and materials Environmental friendly manufacture</p>
      </article>
      <article class="feature">
        <svg viewBox="0 0 34 34"><path d="M7 1h20v32H7zM9.5 3.5v27h15v-27z" fill-rule="evenodd"/><path d="M11.5 6h3v3h-3zm4 0h3v3h-3zm4 0h3v3h-3zm-8 5h3v3h-3zm4 0h3v3h-3zm4 0h3v3h-3zm-8 5h3v3h-3zm4 0h3v3h-3zm4 0h3v3h-3zm-8 5h3v3h-3zm4 0h3v3h-3zm4 0h3v3h-3zm-6 5h4v4.5h-4z"/></svg>
        <h2>Commercial Fit Out Companies</h2>
        <p>Site Surveys and Consulta-tion by our experienced design team</p>
      </article>
      <article class="feature">
        <svg viewBox="0 0 34 34"><path d="M5 2h24v14c0 8-6 13-12 16C11 29 5 24 5 16zM8 5v11c0 6 4 10 9 13V5z" fill-rule="evenodd"/></svg>
        <h2>Awards &amp; Accreditations</h2>
        <p>We are continually looking at how we can improve our services</p>
      </article>
    </section>
  </main>

  <footer class="footer">
    <ul class="footer-nav">
      <li>About Us</li><li>Services</li><li>Our Clients</li><li>Gallery</li><li>Health &amp; Safety</li><li>Specification Sheets</li><li>Contact Us</li>
    </ul>
    <p class="copyright">© 2014. Northvale Architects All rights reserved.</p>
  </footer>
</body>
</html>
```